Business cards for a naturopathic day clinic for stem cell therapy

We need a basic design for a day clinic, that offers stem cell therapies for Lyme therapy and other severe chronic illnesses.
Our name is "Casa velorìn", which can be translated into "Manor Velorbloom". We are a couple of naturopaths working along side physiotherapists and osteopaths, yoga teachers and massage therapists. I attached our logo.

```html
<!DOCTYPE html>
<html lang="en">
<head>
<meta charset="utf-8">
<title>Casa velorìn – Business Cards</title>
<link href="https://fonts.googleapis.com/css2?family=Source+Sans+3:wght@400;600;700&display=swap" rel="stylesheet">
<style>
  :root {
    --backdrop: #e3e3e3;
    --card-dark: #2d2a28;
    --card-light: #f4f4f4;
    --leaf-green: #a9bd5a;
    --taupe: #8d7b70;
    --ink: #2f2f2f;
  }
  * { margin: 0; padding: 0; box-sizing: border-box; }
  html, body {
    width: 1200px; height: 960px; overflow: hidden;
    background: var(--backdrop);
    font-family: "Source Sans 3", "Source Sans Pro", sans-serif;
  }
  .card {
    position: absolute; left: 323px; width: 557px; height: 361px;
  }
  .card-front { top: 103px; background: var(--card-dark); }
  .card-back { top: 504px; background: var(--card-light); }

  .front-brand {
    position: absolute; inset: 0;
    display: flex; align-items: center; justify-content: center; gap: 14px;
  }
  .front-brand .brand-dot {
    width: 22px; height: 22px; border-radius: 50%; background: var(--leaf-green);
  }
  .front-brand .brand-name {
    font-size: 38px; font-weight: 400; color: var(--leaf-green); letter-spacing: 0.5px;
  }

  .back-brand {
    position: absolute; left: 36px; top: 160px;
    display: flex; align-items: center; gap: 10px;
  }
  .back-brand .brand-dot {
    width: 16px; height: 16px; border-radius: 50%; background: var(--taupe);
  }
  .back-brand .brand-name {
    font-size: 30px; font-weight: 400; color: var(--leaf-green);
  }

  .divider {
    position: absolute; left: 277px; top: 86px; width: 2px; height: 188px;
    background: var(--taupe);
  }

  .contact {
    position: absolute; left: 305px; top: 84px; color: var(--ink);
    font-size: 15px; line-height: 20px;
  }
  .contact .person-name { font-size: 19px; font-weight: 600; color: var(--leaf-green); line-height: 24px; }
  .contact .person-role { margin-bottom: 24px; }
  .contact .company { font-size: 14px; font-weight: 700; letter-spacing: 0.2px; }
  .contact .company .accent { color: var(--leaf-green); font-weight: 600; }
  .contact .address { margin-bottom: 7px; }
  .contact-line { display: flex; align-items: center; gap: 5px; }
  .contact-line svg { width: 13px; height: 13px; flex: none; }
</style>
</head>
<body>
  <section class="card card-front">
    <div class="front-brand">
      <span class="brand-dot"></span>
      <span class="brand-name">Casa velorìn</span>
    </div>
  </section>

  <section class="card card-back">
    <div class="back-brand">
      <span class="brand-dot"></span>
      <span class="brand-name">Casa velorìn</span>
    </div>

    <div class="divider"></div>

    <div class="contact">
      <div class="person-name">Jonas Ebersfeld</div>
      <div class="person-role">Founder</div>
      <div class="company"><span class="accent">CASA</span> VELORÌN</div>
      <div class="address">Lindenweg 8<br>64820 Harthausen-Tal</div>
      <div class="contact-line">
        <svg viewBox="0 0 16 16" fill="var(--leaf-green)"><path d="M3.6 1.5l2.3 2.6-1.2 1.6c.8 1.9 2.3 3.4 4.2 4.3l1.6-1.2 2.6 2.2-1.2 2.3C7 13.6 2.4 9 1.6 3.1z"/></svg>
        <span>+49 6100-5550182</span>
      </div>
      <div class="contact-line">
        <svg viewBox="0 0 16 16" fill="none" stroke="var(--leaf-green)" stroke-width="1.6"><rect x="1.5" y="3.5" width="13" height="9"/><path d="M1.5 3.5l6.5 5 6.5-5"/></svg>
        <span>jonas@casa-velorin.de</span>
      </div>
      <div class="contact-line">
        <svg viewBox="0 0 16 16" fill="none" stroke="var(--leaf-green)" stroke-width="1.4"><circle cx="8" cy="8" r="6.3"/><ellipse cx="8" cy="8" rx="2.8" ry="6.3"/><path d="M1.7 8h12.6"/></svg>
        <span>www.casa-velorin.de</span>
      </div>
    </div>
  </section>
</body>
</html>
```